Design concept for BrightKestrel.com Support Page

We are about to launch a new support page for our www.brightkestrel.com service for photographers and visual artists. The service provides media management, cloud storage, promotional and secure distribution to our members.

The support page will include FAQs and video tutorials.

In particular we're looking for a header for this page that suggests the user is in the support area of our service - so perhaps an illustration that suggests support could look nice (perhaps repair man or doctor iconography). Something to give this area of our site a different look and something that looks both cool and friendly.

Currently the page looks distinctly sparse and undesigned (see attached screenshot) - something that could be remedied, we feel, by some subtle design enhancements that we can implement using CSS.

```html
<!DOCTYPE html>
<html lang="en">
<head>
<meta charset="utf-8">
<title>BrightKestrel Support</title>
<link href="https://fonts.googleapis.com/css2?family=Open+Sans:wght@300;400;600;700&display=swap" rel="stylesheet">
<style>
  :root {
    --header-bg: #efefef;
    --header-text: #8a8a8a;
    --brand-text: #5d5d5d;
    --divider: #d6d6d6;
    --hero-top: #5b6470;
    --hero-mid: #3d4452;
    --hero-bottom: #2a2c35;
    --hero-warm: #6b5440;
    --accent: #00b2ef;
    --accent-glow: #1a9fd8;
    --white: #ffffff;
    --body-text: #555555;
    --item-text: #666666;
    --item-border: #dcdcdc;
    --item-top: #fbfbfb;
    --item-bottom: #efefef;
    --icon-dark: #444444;
  }
  * { box-sizing: border-box; margin: 0; padding: 0; }
  html, body { width: 1200px; height: 960px; overflow: hidden; background: var(--white); font-family: "Open Sans", Arial, sans-serif; }
  .page { position: relative; width: 1200px; height: 960px; }

  .site-header { position: absolute; left: 0; top: 0; width: 1200px; height: 90px; background: var(--header-bg); box-shadow: 0 2px 4px rgba(0,0,0,.35); z-index: 2; }
  .brand { position: absolute; left: 58px; top: 22px; display: flex; align-items: center; gap: 12px; }
  .brand-mark { width: 40px; height: 40px; background: var(--brand-text); border-radius: 4px; }
  .brand-name { font-size: 34px; font-weight: 700; color: var(--brand-text); letter-spacing: -0.5px; line-height: 44px; }
  .header-divider { position: absolute; left: 362px; top: 30px; width: 1px; height: 30px; background: var(--divider); }
  .section-label { position: absolute; left: 396px; top: 22px; display: flex; align-items: center; gap: 14px; color: var(--header-text); }
  .section-label svg { width: 28px; height: 30px; }
  .section-label span { font-size: 36px; font-weight: 300; line-height: 46px; }
  .account { position: absolute; left: 1001px; top: 25px; display: flex; align-items: center; }
  .avatar { width: 40px; height: 40px; background: linear-gradient(135deg, #7a3b1e, #c4874e 60%, #3a2a1e); }
  .account-name { margin-left: 15px; font-size: 20px; color: #777; }
  .account-caret { margin-left: 18px; width: 0; height: 0; border-left: 5px solid transparent; border-right: 5px solid transparent; border-top: 8px solid #b0b0b0; }

  .hero { position: absolute; left: 0; top: 90px; width: 1200px; height: 388px;
    background:
      linear-gradient(180deg, rgba(40,44,55,.25), rgba(20,22,30,.55)),
      linear-gradient(90deg, var(--hero-warm) 0%, var(--hero-mid) 35%, #4a4a50 60%, var(--hero-warm) 85%, var(--hero-mid) 100%),
      linear-gradient(180deg, var(--hero-top), var(--hero-bottom)); 
    background-blend-mode: normal, multiply, normal; }
  .hero-title { position: absolute; left: 0; top: 144px; width: 1200px; text-align: center; font-size: 47px; font-weight: 400; color: var(--white); letter-spacing: .5px; }
  .search { position: absolute; left: 292px; top: 261px; width: 616px; height: 56px; border: 2px solid var(--accent-glow); border-radius: 3px; box-shadow: 0 0 6px rgba(0,178,239,.7); display: flex; background: var(--white); }
  .search-input { flex: 1; padding-left: 12px; font-size: 19px; color: #777; line-height: 52px; }
  .search-button { width: 76px; background: var(--accent); display: flex; align-items: center; justify-content: center; }

  .tutorials { position: absolute; left: 294px; top: 522px; width: 607px; }
  .tutorials-heading { display: flex; align-items: center; gap: 20px; margin-left: 2px; height: 36px; }
  .tutorials-heading span { font-size: 25px; font-weight: 300; color: var(--body-text); }
  .topic-list { list-style: none; margin-top: 39px; }
  .topic { height: 62px; margin-bottom: 19px; border: 1px solid var(--item-border); background: linear-gradient(180deg, var(--item-top), var(--item-bottom)); box-shadow: 0 1px 3px rgba(0,0,0,.12); display: flex; align-items: center; padding-left: 24px; }
  .topic-plus { width: 20px; height: 20px; position: relative; margin-right: 20px; }
  .topic-plus::before, .topic-plus::after { content: ""; position: absolute; background: #555; }
  .topic-plus::before { left: 0; top: 8px; width: 20px; height: 3px; }
  .topic-plus::after { left: 8px; top: 0; width: 3px; height: 20px; }
  .topic-title { font-size: 20px; color: var(--item-text); }
</style>
</head>
<body>
<div class="page">
  <header class="site-header">
    <div class="brand">
      <div class="brand-mark"></div>
      <div class="brand-name">BrightKestrel</div>
    </div>
    <div class="header-divider"></div>
    <div class="section-label">
      <svg viewBox="0 0 28 30" fill="none" stroke="currentColor" stroke-width="2.2" stroke-linecap="round">
        <path d="M5 3 L5 11 Q5 18 12 18 Q19 18 19 11 L19 3"/>
        <path d="M12 18 L12 23 Q12 27 16 27 Q21 27 21 22 L21 19"/>
        <circle cx="21" cy="16.5" r="2.5"/>
      </svg>
      <span>Support</span>
    </div>
    <div class="account">
      <div class="avatar" role="img" aria-label="User profile photo"></div>
      <span class="account-name">Anonimus</span>
      <span class="account-caret"></span>
    </div>
  </header>

  <section class="hero" role="img" aria-label="City skyline photograph at dusk">
    <h1 class="hero-title">We’re happy to help...</h1>
    <div class="search">
      <div class="search-input">Search...</div>
      <div class="search-button">
        <svg width="30" height="30" viewBox="0 0 30 30" fill="none" stroke="#ffffff" stroke-linecap="round">
          <circle cx="11" cy="11" r="7" stroke-width="3.5"/>
          <path d="M16.5 16.5 L25 25" stroke-width="5"/>
        </svg>
      </div>
    </div>
  </section>

  <section class="tutorials">
    <div class="tutorials-heading">
      <svg width="30" height="30" viewBox="0 0 30 30">
        <circle cx="15" cy="15" r="14" fill="var(--icon-dark)"/>
        <path d="M11.5 8.5 L21.5 15 L11.5 21.5 Z" fill="#ffffff"/>
      </svg>
      <span>Video tutorial</span>
    </div>
    <ul class="topic-list">
      <li class="topic"><span class="topic-plus"></span><span class="topic-title">Uploading Files Using the Drag &amp; Drop</span></li>
      <li class="topic"><span class="topic-plus"></span><span class="topic-title">Publishing Files</span></li>
      <li class="topic"><span class="topic-plus"></span><span class="topic-title">Creating Galleries</span></li>
    </ul>
  </section>
</div>
</body>
</html>
```